Need A Modern Website Design For ADSL2+ Provider

AIM: To sell affordable combined ADSL2+ Unlimited & phone line rentals to residential customers.

TYPE: This project is for DESIGN only (no code)

Source Files: I need all source files, fonts, images to be provided in ZIP format.

Logo: Existing (attached)

-Corporate Colours-
Black & Red (Same as Logo)
Others colours are fine as long as it looks corporate and modern.

-Pages-
Need another page to display our pricing plan

(1)Homepage Design
(2)Page to display our plans (needs to be in tables)
Example: http://lnkshrt.example/Qv7Rp2

-Pricing Plan-
(1) $59.95 / Month (Metro / City Areas)
(2) $79.95 / Month (Outside City Areas / Rural Areas)
Detailed Pricing plans is in PDF attached
Updates

Just letting everyone know we have picked a designer, thank you for all you submissions.

Target Market(s)

Both male & female, Young & Old

Industry/Entity Type

Residential

Requirements
Must have
• + Graphic banner on the home page that shows our ADSL2+ combo plan for ADSL2+ Unlimited & Phone Line Rental for only $59.95

+ A box to allow customers to login to their account (username & password + login button)

+ Clearly display contact number
+ Button to sign up
+ Button to check service availability something like https://linkup.vexora.com/wizard/

+ Button for Live Chat
+ Navigation menu
+ Social media icons Chatterly, Plexo +, Chirpnet
+ Minimal text on homepage
+ Corporate & Friendly
Nice to have
• + Effective use of icons with corporate colours
+ Effective use of stockphotos
(use of people in photos would be nice)

+ Effective use of graphics to navigate people through the site and inform customers of specials,etc.
Should not have
• + Cluttered
+ Don’t want long scrolling homepage
+ Don’t want too much text on homepage 500 words is the estimate max.

```html
<!DOCTYPE html>
<html lang="en">
<head>
<meta charset="utf-8">
<title>Veltora – ADSL2+ Combo Plans</title>
<link rel="stylesheet" href="https://fonts.googleapis.com/css2?family=Cinzel:wght@400;700&family=EB+Garamond:ital@1&family=PT+Sans:wght@400;700&family=Arimo:wght@400;700&display=swap">
<style>
:root{
  --red:#e00a0a;
  --red-dark:#b80606;
  --red-btn:#e52416;
  --pink:#f08080;
  --ink:#222222;
  --ink-soft:#2b2b2b;
  --white:#ffffff;
  --blue:#2a77a6;
  --yellow:#e9b702;
  --grey-line:#c9c9c9;
  --footer-top:#4a4a4a;
  --footer-bottom:#141414;
}
*{box-sizing:border-box;margin:0;padding:0}
html,body{width:1123px;height:1200px;overflow:hidden;background:var(--red)}
.stage{position:relative;width:1280px;height:1368px;transform:scale(0.87734);transform-origin:0 0;background:var(--red);font-family:"PT Sans",sans-serif;color:var(--white)}
.abs{position:absolute}

/* navigation */
.nav{position:absolute;top:40px;height:35px;border-top:1px solid #fff;border-bottom:1px solid #fff;display:flex;align-items:center;justify-content:space-between;padding:0 6px}
.nav::before,.nav::after{content:"";position:absolute;left:0;right:0;height:1px;background:rgba(255,255,255,.6)}
.nav::before{top:3px}.nav::after{bottom:3px}
.nav a{font-family:"Cinzel",serif;font-size:17px;color:#fff;text-decoration:none;letter-spacing:.5px}
.nav-left{left:140px;width:347px}
.nav-right{left:800px;width:346px}

.brand-frame{left:487px;top:0;width:313px;height:118px;background:var(--pink);border-radius:0 0 14px 14px}
.brand-card{position:absolute;left:13px;top:0;width:285px;height:110px;background:#fff;border-radius:0 0 10px 10px;display:flex;align-items:center;justify-content:center;gap:12px}
.brand-dot{width:48px;height:48px;border-radius:50%;background:var(--ink)}
.brand-name{font-family:"Cinzel",serif;font-size:38px;color:var(--ink);letter-spacing:1px}

.pill{top:103px;width:205px;height:54px;border-radius:27px;background:var(--pink);padding:5px}
.pill span{display:flex;align-items:center;justify-content:center;gap:12px;height:100%;border-radius:22px;background:linear-gradient(#fff,#dcdcdc);color:var(--ink-soft);font-weight:700;font-size:18px}
.pill i{width:32px;height:26px;border-radius:6px;background:#7a8a99;display:block}

/* hero */
.hero{left:140px;top:180px;width:1005px;height:400px;overflow:hidden}
.hero-photo{position:absolute;inset:0;background:linear-gradient(100deg,#d9d4cf 0%,#b89684 30%,#e6e1dc 55%,#cfc9c4 100%)}
.hero-copy{position:absolute;right:26px;top:90px;text-align:right;font-family:"EB Garamond",serif;font-style:italic;font-size:40px;line-height:57px;color:#fff}
.hero-copy em{color:#ff3b2f;font-size:46px}
.dots{position:absolute;right:32px;top:364px;display:flex;gap:6px}
.dots b{width:15px;height:15px;border-radius:50%;background:#fff;display:block}
.dots b.on{background:var(--red-btn);box-shadow:0 0 0 2px #fff}

/* plan cards */
.plan{top:600px;width:317px;height:183px;border-radius:6px 6px 0 0;padding:6px 18px;overflow:hidden;border-bottom:4px solid #333}
.plan-metro{left:145px;background:var(--blue)}
.plan-regional{left:485px;background:var(--yellow)}
.plan h3{font-size:18px;font-weight:700;margin-bottom:6px}
.plan p{font-size:15px;line-height:18px}
.plan p.rate{font-size:14px;margin-top:5px}
.ribbon{position:absolute;right:-38px;top:20px;width:150px;height:24px;background:var(--red-btn);transform:rotate(45deg);text-align:center;font-size:14px;font-weight:700;line-height:24px}
.plan-regional .ribbon{background:var(--ink)}
.btns{position:absolute;left:20px;top:135px;display:flex;gap:12px}
.btn{display:flex;align-items:center;justify-content:space-between;width:120px;height:30px;padding:0 10px;background:var(--red-btn);color:#fff;font-size:14px;font-weight:700;border-radius:2px}
.btn.dark{background:var(--ink)}
.finder{left:818px;top:600px;width:317px;height:183px;background:var(--ink);border-radius:6px 6px 0 0;padding:12px 29px;border-bottom:4px solid #bbb}
.finder h3{font-size:20px;font-weight:700}
.finder p{font-size:20px;margin-top:10px}
.field{height:28px;background:#fff;border:1px solid #ccc;border-radius:3px;color:#999;font-size:13px;padding:5px 12px}
.finder .field{width:240px;margin-top:12px}
.finder .btn{width:90px;margin-top:18px}

/* welcome */
.welcome{left:147px;top:825px;width:346px}
.welcome h2{font-family:"Cinzel",serif;font-size:27px;display:flex;align-items:center;gap:9px;white-space:nowrap}
.welcome h2 i{width:37px;height:37px;border-radius:50%;background:var(--ink);display:block}
.welcome h2 span{color:var(--ink)}
.welcome p{margin-top:18px;font-size:12.4px;line-height:19px;letter-spacing:.35px}
.welcome .more{display:block;text-align:right;margin-top:10px;padding-right:6px;font-weight:700;font-size:14px}

.features{left:525px;top:830px;width:330px;list-style:none}
.features li{display:flex;align-items:center;gap:14px;font-family:"Cinzel",serif;font-size:17px;letter-spacing:.5px}
.features .ico{width:62px;height:52px;display:flex;align-items:center;justify-content:center}
.features .ico i{width:46px;height:46px;border-radius:50%;display:block}

.contact{left:864px;top:824px;width:276px;height:263px;background:linear-gradient(#fff,#ececec);border-radius:8px;padding:14px 19px;color:var(--ink)}
.contact h3{font-family:"Cinzel",serif;font-size:20px;text-align:center;margin-bottom:16px;font-weight:400}
.contact .field{margin-bottom:9px;color:#555}
.contact .msg{height:48px}
.contact .submit{width:75px;height:28px;border-radius:4px;background:linear-gradient(#444,#111);color:#fff;font-size:15px;text-align:center;line-height:28px}
.offer{left:865px;top:1094px;width:276px;height:82px;background:#fff;border-radius:4px;color:var(--ink);padding:12px 10px 0 136px}
.offer .stamp{position:absolute;left:12px;top:16px;width:110px;height:48px;border:3px solid var(--red-btn);border-radius:6px;transform:rotate(-12deg);background:#fde9e7}
.offer p{font-size:13px;font-weight:700;line-height:17px}
.offer a{display:block;text-align:right;margin-top:8px;font-size:12px;font-weight:700}

/* footer */
.footer{left:0;top:1205px;width:1280px;height:163px;background:linear-gradient(var(--footer-top),var(--footer-bottom))}
.footer h4{position:absolute;font-family:"Cinzel",serif;font-size:20px;font-weight:400}
.links{position:absolute;top:52px;list-style:none;font-family:"Arimo",sans-serif;font-size:13px;line-height:23.5px}
.links li::before{content:"> ";color:var(--red-btn)}
.news-field{position:absolute;left:515px;top:53px;width:242px;height:37px;background:#ccc;border-radius:4px;color:#444;font-style:italic;font-size:13px;padding:10px 11px;font-family:"Arimo",sans-serif}
.news-btn{position:absolute;left:515px;top:101px;width:88px;height:37px;background:var(--red-btn);border-radius:4px;text-align:center;line-height:37px;font-weight:700;font-size:15px;letter-spacing:1px}
.foot-brand{position:absolute;left:860px;top:14px;display:flex;align-items:center;gap:12px}
.foot-brand i{width:62px;height:62px;border-radius:50%;background:#fff;display:block}
.foot-brand span{font-family:"Cinzel",serif;font-size:44px}
.social{position:absolute;right:148px;top:80px;display:flex;gap:8px}
.social span{font-family:"Arimo",sans-serif;font-size:10px;border:1px solid #fff;border-radius:4px;padding:4px 5px}
.copy{position:absolute;right:150px;top:120px;font-family:"Arimo",sans-serif;font-size:12px}
</style>
</head>
<body>
<div class="stage">

  <nav class="nav nav-left"><a>Home</a><a>Services</a><a>Member Area</a></nav>
  <nav class="nav nav-right"><a>News</a><a>Special Offers</a><a>Contact</a></nav>

  <div class="abs brand-frame"><div class="brand-card"><i class="brand-dot"></i><span class="brand-name">VELTORA</span></div></div>

  <div class="abs pill" style="left:200px"><span><i></i>Live Chat</span></div>
  <div class="abs pill" style="left:878px"><span><i></i>Login</span></div>

  <section class="abs hero">
    <div class="hero-photo" role="img" aria-label="Photo of a woman talking on a landline phone at her desk"></div>
    <svg class="abs" style="left:0;top:0" width="1005" height="400" viewBox="0 0 1005 400">
      <defs><linearGradient id="edge" x1="0" x2="1"><stop offset="0" stop-color="#555"/><stop offset="1" stop-color="#232323"/></linearGradient></defs>
      <circle cx="880" cy="200" r="348" fill="url(#edge)"/>
      <circle cx="890" cy="200" r="330" fill="#232222"/>
      <rect x="890" y="0" width="115" height="400" fill="#232222"/>
    </svg>
    <div class="hero-copy">ADSL2+ combo plan<br>for ADSL2+ Unlimited<br>&amp; Phone Line Rental<br>for only $ <em>59.95</em></div>
    <div class="dots"><b class="on"></b><b></b><b></b><b></b><b></b></div>
  </section>

  <article class="abs plan plan-metro">
    <div class="ribbon">$59.95/mo</div>
    <h3>Metro On Net</h3>
    <p>Minimum Monthly Charge<br>including line rental and<br>Unlimited ADSL2+</p>
    <p class="rate">29cents $1.89 for first 20 minutes then<br>per minute rate applies</p>
    <div class="btns"><span class="btn">VIEW PLAN <b>➔</b></span><span class="btn">ORDER NOW <b>➔</b></span></div>
  </article>
  <article class="abs plan plan-regional">
    <div class="ribbon">$79.95/mo</div>
    <h3>Regional off Net</h3>
    <p>Minimum Monthly Charge<br>including line rental and<br>Unlimited ADSL2+</p>
    <p class="rate">29cents $1.89 for first 20 minutes then<br>per minute rate applies</p>
    <div class="btns"><span class="btn dark">VIEW PLAN <b>➔</b></span><span class="btn dark">ORDER NOW <b>➔</b></span></div>
  </article>
  <aside class="abs finder">
    <h3>Quick ADSL Plan Finder</h3>
    <p>Check service availability</p>
    <div class="field">Enter Your Phone Number</div>
    <span class="btn">CHECK <b>➔</b></span>
  </aside>

  <section class="abs welcome">
    <h2><i></i>Welcome to <span>Veltora</span></h2>
    <p>Lorem ipsum dolor sit amet, consectetuer adipiscing elit, sed diam nonummy nibh euismod tincidunt ut laoreet dolore magna aliquam erat volutpat. Ut wisi enim ad minim veniam, quis nostrud exerci tation ullamcorper amet suscipit lobortis nisl ut aliquip ex ea commodo consequat. Duis autem vel eum iriure dolor in hendrerit in amet lobortis nisl ut aliquip ex ea commodo consequat. Duis autem vel eum iriure dolor in hendrerit in amet vulputate velitlobortis nisl ut aliquip ex ea commodo consequat. Duis autem vel eum iriure dolor in hendrerit in amet vulputate velit esse molestie consequat, vel illum dolore eu feugiat nulla facilisis at vero eros et accumsan et iust.</p>
    <a class="more">Read More [+]</a>
  </section>

  <ul class="abs features">
    <li style="height:55px"><span class="ico"><i role="img" aria-label="Money back guarantee seal" style="background:#c9961e"></i></span>Money Back Guarantee</li>
    <li style="height:65px;margin-top:4px"><span class="ico"><i role="img" aria-label="24/7 phone support icon" style="background:#3a8fd6"></i></span>24/7 availability</li>
    <li style="height:72px"><span class="ico"><i role="img" aria-label="Globe network icon" style="background:#2f64b8"></i></span>Reliable Network</li>
    <li style="height:72px"><span class="ico"><svg width="40" height="48" viewBox="0 0 40 48"><path d="M4 2h22l10 10v34H4z" fill="none" stroke="#fff" stroke-width="3"/><path d="M10 18h18M10 25h18M10 32h10M28 34v10M23 39h10" stroke="#fff" stroke-width="3"/></svg></span>Easy Contracts</li>
    <li style="height:62px"><span class="ico"><i role="img" aria-label="Open gift box with bargains" style="background:#c8a36b;border-radius:6px"></i></span>Best Bargains</li>
  </ul>

  <section class="abs contact">
    <h3>Quick Contact</h3>
    <div class="field">First Name</div>
    <div class="field">Phone</div>
    <div class="field">Email</div>
    <div class="field msg">Message</div>
    <div class="submit">Submit</div>
  </section>
  <aside class="abs offer">
    <div class="stamp" role="img" aria-label="Red special offer rubber stamp"></div>
    <p>For Unlimited Local<br>and National Calls</p>
    <a>Read More [+]</a>
  </aside>

  <footer class="abs footer">
    <h4 style="left:147px;top:12px">Quick Links</h4>
    <ul class="links" style="left:147px"><li>Home</li><li>Services</li><li>Member Area</li></ul>
    <ul class="links" style="left:318px"><li>News</li><li>Special Offers</li><li>Contact</li></ul>
    <h4 style="left:509px;top:14px">Subscribe to Newsletter</h4>
    <div class="news-field">Email Address</div>
    <div class="news-btn">SUBMIT</div>
    <div class="foot-brand"><i></i><span>VELTORA</span></div>
    <div class="social"><span>Chatterly</span><span>Chirpnet</span><span>Linkora</span></div>
    <div class="copy">Copyright © 2013 veltora. All rights reserved</div>
  </footer>

</div>
</body>
</html>
```